KPL Commercial Realty Group Inc. - 6"x 9" Postcard

Redesigning our Old Postcard (see attached) with updated look and contact information. Minimalism Design Style is appreciated.
KPL Commercial Realty Group, Inc.
555 310 7684
walter@kplhq.com
www.kplhq.com
see our website for updated look and logo

Added Notes 7.3
I do want to stick to the text of the old postcard, just updating the look and current contact info. The Building Images are named for a City Area that we represent and should be included.
Thank You

Added Notes 7.3 I do want to stick to the text of the old postcard, just updating the look and current contact info. The Building Images are named for a City Area that we represent and should be included. Thank You

```html
<!DOCTYPE html>
<html lang="en">
<head>
<meta charset="utf-8">
<title>KPL Commercial Realty Group Inc. – Postcard</title>
<link href="https://fonts.googleapis.com/css2?family=Jost:wght@300;400;500&display=swap" rel="stylesheet">
<style>
  :root {
    --paper: #ffffff;
    --panel: #edf1f0;
    --header-grey: #b3b8b7;
    --ink: #111111;
    --accent-red: #e3191c;
    --brand-red: #e0301e;
  }
  * { margin: 0; padding: 0; box-sizing: border-box; }
  html, body { width: 1200px; height: 800px; overflow: hidden; background: var(--paper); }
  body { font-family: "Jost", "Futura", sans-serif; color: var(--ink); }
  .postcard { position: relative; width: 1200px; height: 800px; background: var(--paper); }

  .masthead { position: absolute; top: 37px; left: 27px; right: 28px; display: flex; justify-content: space-between;
    font-weight: 400; font-size: 32px; letter-spacing: 0.2px; color: var(--header-grey); text-transform: uppercase; white-space: nowrap; }

  .top-band { position: absolute; left: 27px; top: 110px; width: 1145px; height: 58px; background: var(--panel); }

  .building-strip { position: absolute; top: 187px; left: 0; width: 1200px; height: 177px; }
  .building-photo { position: absolute; top: 0; height: 177px; }
  .building-photo.b1 { left: 0; width: 338px; background: linear-gradient(180deg, #c9d6df 0%, #d9c9a8 45%, #c8b894 72%, #7d8470 100%); }
  .building-photo.b2 { left: 344px; width: 236px; background: linear-gradient(180deg, #b8d0e4 0%, #d4dcdf 40%, #b9c1c2 75%, #7f9276 100%); }
  .building-photo.b3 { left: 586px; width: 355px; background: linear-gradient(180deg, #bcd3e6 0%, #e1e3e0 50%, #aab39c 78%, #8c918a 100%); }
  .building-photo.b4 { left: 947px; width: 253px; background: linear-gradient(180deg, #c7dbe9 0%, #dfe2e6 40%, #8ea67a 75%, #6f8d52 100%); }

  .info-panel { position: absolute; left: 27px; top: 383px; width: 1145px; height: 314px; background: var(--panel); }
  .headline { position: absolute; left: 18px; top: 21px; font-size: 38.5px; font-weight: 400; color: var(--accent-red); white-space: nowrap; }

  .agent-photo { position: absolute; left: 26px; top: 162px; width: 117px; height: 127px;
    background: linear-gradient(180deg, #c9ccd0 0%, #9ea3aa 55%, #2a2d35 100%); }
  .agent-card { position: absolute; left: 164px; top: 164px; white-space: nowrap; }
  .agent-name { font-size: 35px; font-weight: 400; line-height: 1; }
  .agent-role { margin-top: 4px; font-size: 22px; font-weight: 400; line-height: 1.2; }
  .agent-links { margin-top: 8px; font-size: 22px; line-height: 26px; }

  .phones { position: absolute; right: 30px; top: 188px; font-size: 37px; font-weight: 400; line-height: 50px; text-align: right; white-space: nowrap; }

  .brand-mark { position: absolute; left: 0; right: 0; top: 724px; display: flex; justify-content: center; align-items: center; gap: 12px;
    font-size: 28px; font-weight: 500; color: var(--ink); letter-spacing: 0.5px; }
  .brand-mark .square { width: 26px; height: 26px; background: var(--brand-red); }
</style>
</head>
<body>
<main class="postcard">
  <header class="masthead">
    <span class="company-name">KPL Commercial Realty Group Inc</span>
    <span class="company-short">KPL Realty</span>
  </header>

  <div class="top-band"></div>

  <section class="building-strip">
    <div class="building-photo b1" role="img" aria-label="Photo of a tan stucco industrial building with parked car, city area one"></div>
    <div class="building-photo b2" role="img" aria-label="Photo of a modern glass and concrete office entrance, city area two"></div>
    <div class="building-photo b3" role="img" aria-label="Photo of a long industrial building with palm trees, city area three"></div>
    <div class="building-photo b4" role="img" aria-label="Photo of a blue-trimmed industrial building behind flowering trees, city area four"></div>
  </section>

  <section class="info-panel">
    <h1 class="headline">Put Over 20 Years of Industrial Real Estate Experience on Your Side</h1>

    <div class="agent-photo" role="img" aria-label="Portrait photo of the agent"></div>
    <div class="agent-card">
      <p class="agent-name">Marcus T. Delwin</p>
      <p class="agent-role">Commercial &amp; Industrial Real Estate Services</p>
      <p class="agent-links">walter@kplhq.com<br>www.kplhq.com</p>
    </div>

    <p class="phones">(555) 482 - 1930<br>(555) 310 - 7684</p>
  </section>

  <footer class="brand-mark">
    <span class="square"></span>
    <span class="brand-name">KPL Realty</span>
  </footer>
</main>
</body>
</html>
```